BRIGHTWATER RV Resort needs a logo and advertising poster

We need an advertising poster for our epic RV Resort located on north end of Tuskin Lake, (Northern Saskatchewan, trees no mountains)
SEASONAL FULL SERVICE SITES with marina and lake access.
Sauna/plunge, disc golf , hiking/quad trails, and pet friendly.
We are after a fun 70,s themed simple poster. Please use brand guide for colours and redo logo to be Brightwater Resort.

Target Market(s)

RV owners looking for permeant sites. No tenting.

Font styles to use
Other font styles liked:
• See brand guide

Requirements
Must have
• Change exisiting branding to BRIGHTWATER RESORT instead of coffee Emphasis Limited sites.... Referral discount. Phone number.
Nice to have
• .
Should not have
• Keep it simple

```html
<!DOCTYPE html>
<html lang="en">
<head>
<meta charset="utf-8">
<title>Brightwater Resort – Campground Poster</title>
<link rel="stylesheet" href="https://fonts.googleapis.com/css2?family=Anton&family=Barlow+Condensed:ital,wght@1,600&family=Montserrat:wght@700;900&display=swap">
<style>
  :root {
    --page-bg: #e9e6df;
    --green: #6f8f52;
    --green-light: #8aa86a;
    --green-pale: #9cb57f;
    --gold: #e6c766;
    --cream: #f8f4e3;
    --ink: #1d1d1b;
    --photo-top: #3f4a3a;
    --photo-mid: #7a6a48;
    --photo-bottom: #4a3a2a;
  }
  * { margin: 0; padding: 0; box-sizing: border-box; }
  html, body {
    width: 1200px; height: 831px; overflow: hidden;
    background: var(--page-bg);
  }
  .stage {
    width: 1200px; height: 831px;
    display: flex; align-items: center; justify-content: center;
  }
  .poster { display: block; width: 592px; height: 831px; }
  .headline { font-family: "Anton", Impact, sans-serif; }
  .list-text { font-family: "Barlow Condensed", "Arial Narrow", sans-serif; font-style: italic; font-weight: 600; }
  .badge-text, .brand-name, .phone { font-family: "Montserrat", Arial, sans-serif; }
</style>
</head>
<body>
<main class="stage">
  <svg class="poster" viewBox="0 0 1130 1596" xmlns="http://www.w3.org/2000/svg" aria-label="Brightwater Resort campground poster">
    <defs>
      <linearGradient id="photoTone" x1="0" y1="0" x2="0" y2="1">
        <stop offset="0" stop-color="var(--photo-top)"/>
        <stop offset="0.55" stop-color="var(--photo-mid)"/>
        <stop offset="1" stop-color="var(--photo-bottom)"/>
      </linearGradient>
    </defs>

    <rect class="poster-bg" width="1130" height="1596" fill="var(--green)"/>

    <g class="corner-bars" fill="var(--green-pale)" opacity="0.55">
      <path d="M0 50 H420 Q440 50 430 75 L420 110 H0 Z"/>
      <path d="M0 170 H360 Q380 170 370 195 L355 240 H0 Z"/>
    </g>

    <path class="photo-area" role="img" aria-label="Photo of a lakeside forest campsite at sunset with a picnic table and a campfire"
      fill="url(#photoTone)"
      d="M0 470 L1130 265 L1130 1165 L0 1000 Z"/>

    <path class="torn-edge" fill="var(--cream)" d="M0 462 L1130 258 L1130 272 L0 478 Z"/>
    <path class="torn-edge" fill="var(--cream)" d="M0 995 L1130 1160 L1130 1172 L0 1008 Z"/>

    <!-- brand name -->
    <g class="brand" fill="var(--cream)" text-anchor="middle">
      <text class="brand-name" x="565" y="130" font-size="58" font-weight="700">BRIGHTWATER</text>
      <text class="brand-name" x="565" y="192" font-size="46" font-weight="700" letter-spacing="8">RESORT</text>
    </g>

    <!-- headline -->
    <g class="headline" transform="rotate(-6 560 450)">
      <text x="180" y="405" font-size="140" fill="var(--gold)" textLength="770" lengthAdjust="spacingAndGlyphs">CANADA’S COOLEST</text>
      <text x="80" y="640" font-size="240" fill="var(--cream)" textLength="990" lengthAdjust="spacingAndGlyphs">CAMPGROUND!</text>
    </g>

    <!-- limited sites -->
    <g class="headline limited" fill="var(--gold)">
      <text x="40" y="1010" font-size="148" textLength="525" lengthAdjust="spacingAndGlyphs">LIMITED SITES</text>
      <text x="40" y="1140" font-size="148" textLength="415" lengthAdjust="spacingAndGlyphs">AVAILABLE!</text>
    </g>

    <!-- referral badge -->
    <g class="badge">
      <circle cx="910" cy="1115" r="160" fill="var(--gold)"/>
      <g transform="rotate(-12 910 1115)" class="badge-text" fill="var(--ink)" text-anchor="middle">
        <text x="910" y="1105" font-size="100" font-weight="900">5%</text>
        <text x="910" y="1155" font-size="42" font-weight="700">REFERRAL</text>
        <text x="910" y="1197" font-size="42" font-weight="700">DISCOUNT</text>
      </g>
    </g>

    <!-- amenities list -->
    <g class="amenities">
      <g fill="var(--green-light)" stroke="var(--cream)" stroke-width="3">
        <rect x="43" y="1180" width="507" height="70" rx="6"/>
        <rect x="43" y="1255" width="507" height="70" rx="6"/>
        <rect x="43" y="1330" width="507" height="70" rx="6"/>
        <rect x="43" y="1405" width="507" height="70" rx="6"/>
        <rect x="43" y="1480" width="507" height="70" rx="6"/>
      </g>
      <g class="list-text" font-size="38" fill="var(--cream)">
        <text x="82" y="1229">1 - Seasonal Full-Service Sites</text>
        <text x="82" y="1304">2 - Marina &amp; Lake Access</text>
        <text x="82" y="1379">3 - Sauna/Plunge</text>
        <text x="82" y="1454">4 - Disc Golf, Hiking &amp; Quad Trails</text>
        <text x="82" y="1529">5 - Pet-Friendly</text>
      </g>
    </g>

    <!-- call to action -->
    <g class="headline cta" fill="var(--cream)" text-anchor="end">
      <text x="1085" y="1415" font-size="115" textLength="395" lengthAdjust="spacingAndGlyphs">BOOK YOUR</text>
      <text x="1085" y="1522" font-size="115" textLength="450" lengthAdjust="spacingAndGlyphs">SPOT TODAY!</text>
    </g>
    <text class="phone" x="1085" y="1572" text-anchor="end" font-size="36" font-weight="700" fill="var(--gold)">(306) 555-0147</text>
  </svg>
</main>
</body>
</html>
```